QuillMark Business Cards

I need a business card designed for QuillMark. To get an idea of what we do please visit https://formvault.example/para-creadores-3

```html
<!DOCTYPE html>
<html lang="en">
<head>
<meta charset="utf-8">
<title>QuillMark Business Cards</title>
<link rel="stylesheet" href="https://fonts.googleapis.com/css2?family=Roboto:ital,wght@0,300;0,400;0,700;1,400&display=swap">
<style>
  :root{
    --ink:#252c37;
    --ink-soft:#2f3642;
    --amber:#e39025;
    --slate:#6b7078;
    --band:#808080;
    --paper:#ffffff;
  }
  *{margin:0;padding:0;box-sizing:border-box}
  html,body{width:960px;height:1200px;overflow:hidden;background:var(--paper)}
  body{position:relative;font-family:"Roboto",Helvetica,Arial,sans-serif}
  .backdrop{position:absolute;left:0;top:0;width:960px;height:1200px}
  .card{position:absolute;left:99px;width:761px;background:var(--ink);border-radius:36px;overflow:hidden}
  .card--front{top:115px;height:443px}
  .card--back{top:597px;height:445px}
  .abs{position:absolute}

  /* front */
  .crystal-art{left:0;top:240px;width:330px;height:210px;
    background:linear-gradient(160deg,rgba(107,112,120,.45),rgba(107,112,120,.15));
    clip-path:polygon(20% 8%,100% 0,68% 100%,0 100%,0 70%)}
  .front-brand{left:221px;top:87px;width:110px;text-align:center;color:var(--amber);font-size:20px;font-weight:700}
  .name-ribbon{left:321px;top:62px;width:440px;height:80px}
  .person{right:72px;top:70px;text-align:center;line-height:1}
  .person__name{font-size:36px;color:var(--amber);font-weight:400}
  .person__name b{color:var(--ink);font-weight:700}
  .person__role{display:block;margin-top:4px;font-size:23px;color:var(--amber);letter-spacing:.5px}
  .icon-rail{left:378px;top:174px;width:60px;height:203px;background:var(--amber);border-radius:30px 30px 0 0}
  .icon-rail-foot{left:378px;top:386px;width:60px;height:57px;background:var(--amber)}
  .icon{position:absolute;left:16px;width:28px;height:28px}
  .contacts{left:458px;top:200px;list-style:none;font-size:17px;color:var(--paper)}
  .contacts li{height:38px;line-height:20px}
  .contacts .accent{color:var(--amber)}

  /* back */
  .pattern{top:0;height:445px;width:160px;
    background:linear-gradient(180deg,rgba(160,120,60,.22),rgba(120,126,136,.18))}
  .pattern--left{left:0}
  .pattern--right{right:0;width:140px}
  .mark-dot{left:169px;top:120px;width:94px;height:94px;border:3px solid var(--amber);border-radius:50%}
  .wordmark{left:290px;top:138px;font-size:40px;font-weight:300;color:var(--paper);letter-spacing:14px;line-height:1}
  .tagline{left:292px;top:185px;font-size:11px;color:var(--amber);letter-spacing:6.4px}
  .tagline-rule{left:478px;top:191px;width:125px;height:1px;background:var(--paper)}
  .web-band{left:0;top:317px;width:761px;height:44px;background:var(--amber)}
  .web-pill{left:230px;top:315px;width:298px;height:48px;background:var(--ink);border-radius:24px;
    color:var(--paper);font-style:italic;font-size:23px;text-align:center;line-height:48px}
</style>
</head>
<body>
  <svg class="backdrop" viewBox="0 0 960 1200" aria-hidden="true">
    <polygon points="2,413 960,121 960,833 2,1125" fill="var(--band)"/>
  </svg>

  <section class="card card--front">
    <div class="abs crystal-art" role="img" aria-label="Large faint geometric crystal decoration"></div>
    <div class="abs front-brand">QuillMark</div>
    <svg class="abs name-ribbon" viewBox="0 0 440 80" aria-hidden="true">
      <polygon points="0,0 440,0 440,80 2,80 23,40" fill="var(--paper)"/>
    </svg>
    <div class="abs person">
      <div class="person__name">Dana <b>Voss</b></div>
      <span class="person__role">PRESIDENT</span>
    </div>

    <div class="abs icon-rail">
      <svg class="icon" style="top:20px" viewBox="0 0 28 28" aria-label="Phone"><circle cx="14" cy="14" r="14" fill="#fff"/><rect x="9" y="7" width="10" height="14" rx="2" fill="none" stroke="var(--amber)" stroke-width="2"/><line x1="12" y1="18" x2="16" y2="18" stroke="var(--amber)" stroke-width="1.6"/></svg>
      <svg class="icon" style="top:58px" viewBox="0 0 28 28" aria-label="Location"><circle cx="14" cy="14" r="14" fill="#fff"/><path d="M14 21c-4-5-5-7-5-9a5 5 0 0 1 10 0c0 2-1 4-5 9z" fill="none" stroke="var(--amber)" stroke-width="1.8"/><circle cx="14" cy="12" r="1.8" fill="var(--amber)"/></svg>
      <svg class="icon" style="top:96px" viewBox="0 0 28 28" aria-label="Social handle"><circle cx="14" cy="14" r="14" fill="#fff"/><circle cx="14" cy="14" r="5" fill="var(--amber)"/></svg>
      <svg class="icon" style="top:134px" viewBox="0 0 28 28" aria-label="Professional network"><circle cx="14" cy="14" r="14" fill="#fff"/><rect x="9" y="9" width="10" height="10" fill="var(--amber)"/></svg>
      <svg class="icon" style="top:172px" viewBox="0 0 28 28" aria-label="Website"><circle cx="14" cy="14" r="14" fill="#fff"/><circle cx="14" cy="14" r="7" fill="none" stroke="var(--amber)" stroke-width="1.8"/><ellipse cx="14" cy="14" rx="3" ry="7" fill="none" stroke="var(--amber)" stroke-width="1.4"/><line x1="7" y1="14" x2="21" y2="14" stroke="var(--amber)" stroke-width="1.4"/></svg>
    </div>
    <div class="abs icon-rail-foot"></div>

    <ul class="abs contacts">
      <li class="accent">+1 555-014-2791</li>
      <li>&nbsp;Lakeview, Minnesota 55400, US</li>
      <li>quill_mark</li>
      <li>FormVault</li>
      <li class="accent">https://www.formvault.example</li>
    </ul>
  </section>

  <section class="card card--back">
    <div class="abs pattern pattern--left" role="img" aria-label="Scattered small crystal pattern"></div>
    <div class="abs pattern pattern--right" role="img" aria-label="Scattered small crystal pattern"></div>
    <div class="abs mark-dot"></div>
    <div class="abs wordmark">QUILLMARK</div>
    <div class="abs tagline">DIGITAL NOTARY</div>
    <div class="abs tagline-rule"></div>
    <div class="abs web-band"></div>
    <div class="abs web-pill">www.formvault.example</div>
  </section>
</body>
</html>
```